Fold up small biz card size flyer for Waxing Salon

To design a simple informative flyer which can fold 3 times measuring 2" x 9" for Waxing Salon in Toronto ON CanadaMy client would like both sides of flyer to have text i.e. the first half of flyer text on front and second half with address etc on back.She doesn;t want a company name as yet but would like maybe the simple shape of a body as in this sample deisign with a stone background.the other pics are just samples of ideas she has suggessted and if there is any text it should simply be wax or waxing or maybe body waxing.Please don't hesitate to ask quesition and i look forward to your submissions.

Target Market(s)

women amd men of all adult ages

Font styles to use
Serif
Sans Serif
Decorative
Script

Colors

Designer to choose colors to be used in the design.

Requirements
Must have
• Fold into three to biz card size so PLEASE STRICTLY 2 INCHES X 9 INCHES AND FOLDED DOWN TO A 2 X 3 BIZ CARD
• Due to small size of flyer there will have to be text on back as well
• thanks for your time and patience
Nice to have
• the images are simply ideas of existing brands...just stone background with perhadps small body shaped graphic no company name
Should not have
• scanitly clad women preferably small body shoped graphic only please/

```html
<!DOCTYPE html>
<html lang="en">
<head>
<meta charset="utf-8">
<title>Body Waxing Fold Flyer</title>
<link rel="stylesheet" href="https://fonts.googleapis.com/css2?family=Oswald:wght@400;500;600&family=Great+Vibes&family=Open+Sans:wght@400;600;700&display=swap">
<style>
  :root {
    --page: #e6e4e1;
    --mauve: #b98489;
    --mauve-dark: #9c7175;
    --blush: #f3b3a3;
    --coral: #e47f6a;
    --white: #ffffff;
    --ink: #2d2a2a;
    --ink-soft: #555050;
    --photo-light: #fbeeee;
    --photo-mid: #efc9c6;
    --photo-skin: #d9a893;
  }
  * { box-sizing: border-box; margin: 0; padding: 0; }
  html, body { width: 874px; height: 1200px; overflow: hidden; }
  body {
    background: var(--page);
    font-family: "Open Sans", Arial, sans-serif;
    position: relative;
  }
  .strip {
    position: absolute;
    top: 115px;
    width: 254px;
    height: 1070px;
    background: var(--mauve);
    overflow: hidden;
    box-shadow: 0 4px 12px rgba(0,0,0,0.25);
  }
  .strip--outside { left: 127px; }
  .strip--inside { left: 503px; }

  .panel { position: absolute; left: 0; width: 254px; }
  .panel--front { top: 0; height: 347px; background: var(--mauve-dark); }
  .panel--back { top: 347px; height: 334px; }
  .panel--inner { top: 681px; height: 389px; background: var(--white); }

  .front-art { position: absolute; inset: 0; }

  .btn-book {
    position: absolute;
    left: 50%;
    transform: translateX(-50%);
    width: 152px;
    height: 18px;
    background: var(--blush);
    color: var(--white);
    font-family: "Oswald", sans-serif;
    font-weight: 500;
    font-size: 9.5px;
    letter-spacing: 0.3px;
    line-height: 18px;
    text-align: center;
  }
  .panel--front .btn-book { top: 300px; }
  .panel--back .btn-book { top: 118px; }

  .share-line {
    position: absolute;
    top: 28px; left: 0; right: 0;
    text-align: center;
    color: var(--white);
    font-family: "Great Vibes", cursive;
    font-size: 18px;
    line-height: 24px;
  }
  .location {
    position: absolute;
    left: 0; right: 0;
    text-align: center;
    color: var(--white);
    font-size: 9px;
    line-height: 12.5px;
  }
  .location--east { top: 146px; }
  .location--north { top: 228px; }

  .inner-photo { position: absolute; top: 0; left: 0; width: 254px; height: 105px; }
  .deal-title {
    position: absolute; top: 112px; left: 14px;
    font-family: "Oswald", sans-serif; font-weight: 600;
    color: var(--coral); font-size: 16px;
  }
  .price-tab {
    position: absolute; left: 14px;
    height: 16px; padding: 0 8px 0 4px;
    background: var(--blush);
    color: var(--white);
    font-family: "Oswald", sans-serif; font-weight: 500;
    font-size: 10.5px; line-height: 16px;
    border-radius: 0 8px 8px 0;
  }
  .price-tab--waxing { top: 136px; }
  .price-tab--polish { top: 311px; }
  .price-tab b { color: var(--coral); font-weight: 600; }
  .deal-note {
    position: absolute; top: 157px; left: 14px; width: 226px;
    color: var(--ink); font-size: 9.5px; font-weight: 700;
  }
  .deal-fine {
    position: absolute; top: 171px; left: 14px; width: 226px;
    color: var(--ink-soft); font-size: 7.5px; line-height: 10px;
  }
  .deal-body {
    position: absolute; top: 230px; left: 14px; width: 226px;
    color: var(--ink-soft); font-size: 7.8px; line-height: 11.5px;
    text-align: justify;
  }
  .deal-tagline {
    position: absolute; top: 340px; left: 14px;
    color: var(--ink); font-size: 8px;
  }
  .polish-photo {
    position: absolute; top: 318px; left: 176px;
    width: 70px; height: 70px; border-radius: 50%;
    background: radial-gradient(circle at 45% 40%, var(--photo-light), var(--photo-skin));
    border: 3px solid var(--white);
    box-shadow: 0 0 0 1px var(--photo-mid);
  }

  .portrait {
    position: absolute; top: 24px; left: 78px;
    width: 98px; height: 98px; border-radius: 50%;
    border: 5px solid #e8c6c4;
    background: radial-gradient(circle at 50% 45%, #f6e2dc, #d9b0a4 70%, #c49a90);
  }
  .value-title {
    position: absolute; top: 158px; left: 0; right: 0;
    text-align: center; color: var(--white);
    font-family: "Oswald", sans-serif; font-weight: 500;
    font-size: 22px; line-height: 27px; letter-spacing: 0.5px;
  }
  .value-bar {
    position: absolute; top: 223px; left: 28px; width: 198px; height: 19px;
    background: var(--blush); color: var(--white);
    font-family: "Oswald", sans-serif; font-weight: 500;
    font-size: 11px; line-height: 19px; text-align: center;
    letter-spacing: 0.3px;
  }
  .value-terms {
    position: absolute; top: 250px; left: 30px; width: 194px;
    text-align: center; color: var(--white);
    font-size: 9px; line-height: 12.5px;
  }
  .service-list {
    position: absolute; left: 18px;
    list-style: none; color: var(--white);
    font-size: 10px; line-height: 17.3px;
  }
  .service-list--first { top: 356px; }
  .service-list--second { top: 689px; }
  .note-heading {
    position: absolute; top: 928px; left: 0; right: 0;
    text-align: center; color: var(--white);
    font-family: "Great Vibes", cursive; font-size: 22px;
  }
  .note-rule {
    position: absolute; top: 944px; height: 1px; width: 60px;
    background: rgba(255,255,255,0.6);
  }
  .note-rule--left { left: 36px; }
  .note-rule--right { right: 36px; }
  .note-list {
    position: absolute; top: 968px; left: 0; right: 0;
    list-style: none; text-align: center; color: var(--white);
    font-size: 10px; line-height: 13.5px;
  }
</style>
</head>
<body>

<section class="strip strip--outside" aria-label="Outside of flyer">
  <div class="panel panel--front">
    <svg class="front-art" width="254" height="347" viewBox="0 0 254 347">
      <defs>
        <linearGradient id="heroTone" x1="0" y1="0" x2="1" y2="1">
          <stop offset="0" stop-color="#f9e6e6"/>
          <stop offset="0.5" stop-color="#f0cdc8"/>
          <stop offset="1" stop-color="#fbeeee"/>
        </linearGradient>
      </defs>
      <rect x="88" y="12" width="78" height="26" rx="13" fill="#ad8488" role="img" aria-label="Small line drawing of a reclining body"/>
      <path d="M0 48 Q127 30 254 48 L254 262 Q140 300 0 282 Z" fill="url(#heroTone)" role="img" aria-label="Photo of a woman's waist and hips wrapped in a towel"/>
      <path d="M0 282 Q140 300 254 262 L254 272 Q140 310 0 290 Z" fill="#ffffff" opacity="0.7"/>
    </svg>
    <div class="btn-book">CALL TODAY TO BOOK A SPOT</div>
  </div>

  <div class="panel panel--back">
    <p class="share-line">Services may be<br>Shared with your<br>Loved Ones</p>
    <div class="btn-book">CALL TODAY TO BOOK A SPOT</div>
    <address class="location location--east" style="font-style:normal">
      1250 MAPLE ROW EAST<br>
      #3 Toronto ON M0A 1A1<br>
      Opp to Cedar Grill House<br>
      (416) 555-0142 | 1 (833) 555-0187
    </address>
    <address class="location location--north" style="font-style:normal">
      1470 Birchwood Ave,<br>
      #3, North York, ON M0B 2B2<br>
      Opp to Elm Square Next to Corner Mart<br>
      (416) 555-0199 | 1 (833) 555-0163
    </address>
  </div>

  <div class="panel panel--inner">
    <svg class="inner-photo" width="254" height="105" viewBox="0 0 254 105">
      <defs>
        <radialGradient id="bokehTone" cx="0.3" cy="0.4" r="0.9">
          <stop offset="0" stop-color="#fbe9ec"/>
          <stop offset="0.55" stop-color="#eec2c6"/>
          <stop offset="1" stop-color="#d9a893"/>
        </radialGradient>
      </defs>
      <path d="M0 0 H254 V82 Q130 110 0 92 Z" fill="url(#bokehTone)" role="img" aria-label="Photo of smooth legs on a soft pink bokeh background"/>
    </svg>
    <h2 class="deal-title">DOOR BUSTER DEAL !</h2>
    <div class="price-tab price-tab--waxing"><b>$66</b> BODY WAXING</div>
    <p class="deal-note">For women only!</p>
    <p class="deal-fine">(Neck to Toe- Including Brazilian) with Take Home Scrub used to improve in-grown body hair.</p>
    <p class="deal-body">Guests receive full body waxing during one appointment on the following areas: butt, hollywood, bikini, underarms, stomach, cleavage, full back, fullarms &amp; full legs.</p>
    <div class="price-tab price-tab--polish"><b>$88</b> BODY POLISHING</div>
    <p class="deal-tagline">The secret to soft, smooth skin.</p>
    <div class="polish-photo" role="img" aria-label="Round photo of smooth polished legs"></div>
  </div>
</section>

<section class="strip strip--inside" aria-label="Inside of flyer">
  <div class="portrait" role="img" aria-label="Round portrait photo for facial treatments"></div>
  <h1 class="value-title">UNBEATABLE<br>VALUE !</h1>
  <div class="value-bar">$13 SPA TREATMENTS</div>
  <p class="value-terms">$13 each when you purchase 5 services or more from list below</p>

  <ol class="service-list service-list--first">
    <li>1. Back Massage</li>
    <li>2. Back Scrub</li>
    <li>3. Spa Manicure</li>
    <li>4. Full Brazilian Wax</li>
    <li>5. Full 60 Minute Facial</li>
    <li>6. Face Polishing</li>
    <li>7. Face Bleaching</li>
    <li>8. Scalp &amp; Hair Oil Massage</li>
    <li>9. Dry Hair Treatment</li>
    <li>10. Hair Colour Application</li>
    <li>11. Four Inch Henna Tattoo</li>
    <li>12. Eyebrow Tinting/Shaping</li>
    <li>13. Upper Lip Thread/wax</li>
    <li>14. Forehead Thread/wax</li>
    <li>15. Side Burn Thread/Wax</li>
    <li>16. Full Face Thread/Wax</li>
    <li>17. Nostril Wax</li>
    <li>18. Nape Wax</li>
  </ol>

  <ol class="service-list service-list--second">
    <li>19. Cleavage Wax</li>
    <li>20. Stomach Wax</li>
    <li>21. Upper Back Wax</li>
    <li>22. Lower Back Wax</li>
    <li>23. Underarm Wax</li>
    <li>24. Half Arm Wax</li>
    <li>25. Full Arm Wax</li>
    <li>26. Half Legs Wax</li>
    <li>27. Full Legs Wax</li>
    <li>28. Bikini Line Wax</li>
    <li>29. Bum Wax</li>
    <li>30. Hollywood Wax</li>
  </ol>

  <span class="note-rule note-rule--left"></span>
  <h3 class="note-heading">Note</h3>
  <span class="note-rule note-rule--right"></span>
  <ul class="note-list">
    <li>#3 $5 extra for nail polish</li>
    <li>#4 counts as 2 services</li>
    <li>#5 counts as 3 services</li>
  </ul>
</section>

</body>
</html>
```